Engineering and Energy service provider

We need a design that gives the impression of a high level of technical competence and a reliable partner. Simple structure with little need for updates.
The company brand is Volnar and today consists of two main businesses: energy optimisation (Volnar energy) and technical consultancy (Volnar Engineering). Volnar energy is shown in the attached powerpoint,
We are a young growing company that consists of several businesses, the largest parts are energy monitoring services and consulting services. Consulting services for commercial installations in the technical area of cooling, ventilation, heating and energy. Services offered include project planning, project management, inspection, operational analysis and technical investigations. Energy monitoring and optimization services are performed as a subscription with a subscription to the service.
Target Market(s)
Commercial property owners Grocery retail, grocery stores, construction companies
Industry/Entity Type
energy services and consulting services
Coding
Coded - Design and coding required
Number of Pages Required
5+ page
Look and feel
Each slider illustrates characteristics of the customer's brand and the style your logo design should communicate.

```html
<!DOCTYPE html>
<html lang="en">
<head>
<meta charset="utf-8">
<title>Volnar — Energy and Engineering</title>
<link rel="stylesheet" href="https://fonts.googleapis.com/css2?family=Montserrat:wght@500;600;700;800&family=Figtree:wght@400;500;600&display=swap">
<style>
:root{
  --blue:#0d47c0;
  --blue-deep:#0a3596;
  --blue-ink:#0c3a9e;
  --blue-light:#eaf4fc;
  --navy:#0a1630;
  --white:#ffffff;
  --text:#1d2540;
  --accent:#2a63e0;
}
*{margin:0;padding:0;box-sizing:border-box}
html,body{width:1200px;height:3829px;overflow:hidden}
body{font-family:"Figtree",sans-serif;color:var(--text);background:var(--white)}
.h{font-family:"Montserrat",sans-serif;font-weight:800;text-transform:uppercase}
section,header,footer{position:relative;width:1200px;overflow:hidden}
.abs{position:absolute}
.btn{position:absolute;display:flex;align-items:center;justify-content:center;border-radius:30px;font-family:"Montserrat",sans-serif;font-weight:700;text-transform:uppercase}
.btn-blue{background:var(--blue);color:var(--white)}
.btn-white{background:var(--white);color:var(--blue)}
.rule{position:absolute;height:2px;width:54px}
.wordmark{font-family:"Montserrat",sans-serif;font-weight:800;letter-spacing:4px}

/* hero */
.hero{height:669px;background:linear-gradient(180deg,#0a1428 0%,#142a55 45%,#3b4d86 72%,#6a5c8e 86%,#2a2434 100%)}
.hero .photo{position:absolute;inset:0}
.nav-logo{left:149px;top:28px;font-size:32px;color:var(--blue)}
.nav{left:422px;top:34px;display:flex;font-family:"Figtree",sans-serif;font-size:14px;color:var(--white);font-weight:500}
.nav span{padding:5px 10px;margin-right:9px;border-radius:16px}
.nav .active{background:var(--blue)}
.hero-title{left:0;width:1200px;top:128px;text-align:center;color:var(--white);font-size:36px;line-height:45px}
.hero-title em{font-style:normal;color:var(--blue)}
.dots{left:554px;top:617px;display:flex;gap:11px}
.dots i{width:13px;height:13px;border-radius:50%;border:1.5px solid #c9d4ec}
.dots i.on{background:var(--accent);border-color:var(--accent)}

/* welcome */
.welcome{height:458px;background:radial-gradient(circle at 95% 80%,#1a55d0 0%,var(--blue) 45%,var(--blue-deep) 100%)}
.welcome .photo{left:150px;top:51px;width:454px;height:350px;border-radius:12px;background:linear-gradient(135deg,#c9d6e2,#7f97b0 50%,#2d3f63)}
.welcome h2{left:659px;top:42px;color:var(--white);font-size:37px;line-height:44px}
.welcome .rule{left:659px;top:148px;background:var(--white)}
.welcome p{left:659px;top:180px;width:392px;color:var(--white);font-size:14px;line-height:19.5px}

/* core areas */
.core{height:669px}
.core h2{left:0;width:1200px;top:52px;text-align:center;font-size:32px;color:#0a0f1f}
.core h2 em{font-style:normal;color:var(--blue)}
.core .rule{left:583px;top:116px;width:34px;background:var(--blue)}
.area{position:absolute;top:160px;width:440px;height:446px;border-radius:12px}
.area.one{left:149px;background:var(--blue-light)}
.area.two{left:610px;background:var(--white);border:1.5px solid #7d98d8}
.area .photo{position:absolute;left:14px;top:14px;width:412px;height:223px;border-radius:12px}
.area.one .photo{background:linear-gradient(135deg,#dfe6ee,#9aabbd 55%,#2752b8)}
.area.two .photo{background:linear-gradient(180deg,#3a7bd5 0%,#9cc3ea 40%,#c9ccd1 70%,#6f7680)}
.brandrow{position:absolute;left:34px;top:265px;display:flex;align-items:center}
.brandrow .wordmark{font-size:25px;color:var(--blue-ink);letter-spacing:3px}
.brandrow .sep{width:2px;height:40px;background:var(--blue-ink);margin:0 22px}
.brandrow .sub{font-family:"Montserrat",sans-serif;font-weight:700;font-size:17px;line-height:21px;color:var(--blue-ink);text-transform:uppercase}
.area p{position:absolute;left:34px;top:330px;width:380px;font-size:14px;line-height:19px}
.area .btn{left:34px;top:388px;width:106px;height:32px;font-size:12px}

/* why */
.why{height:510px;background:var(--blue-light)}
.why .band{left:0;top:0}
.why .big{left:149px;top:62px;font-size:60px;color:var(--white);letter-spacing:8px}
.why h2{left:149px;top:185px;color:var(--white);font-size:32px;line-height:40px}
.why .rule{left:149px;top:280px;width:34px;background:var(--white)}
.why p{left:149px;top:308px;width:290px;color:var(--white);font-size:14.5px;line-height:19.5px}
.why .btn{left:149px;top:379px;width:137px;height:38px;font-size:13px}
.feat{position:absolute;display:flex;align-items:flex-start}
.feat .ico{width:68px;height:68px;border-radius:50%;background:var(--white);box-shadow:0 4px 12px rgba(13,71,192,.2);display:flex;align-items:center;justify-content:center;flex:none}
.feat .txt{margin-left:26px;margin-top:-12px}
.feat h3{font-family:"Montserrat",sans-serif;font-weight:700;font-size:15px;color:var(--blue-ink);text-transform:uppercase;margin-bottom:6px}
.feat p{position:static;width:380px;color:var(--text);font-size:12px;line-height:16px}

/* energy */
.energy{height:538px}
.energy .mark{left:0;width:1200px;top:66px;text-align:center}
.energy .mark .wordmark{font-size:46px;color:var(--blue-ink);letter-spacing:6px;line-height:50px}
.energy .mark .tag{font-family:"Montserrat",sans-serif;font-weight:600;font-size:13px;letter-spacing:9px;color:var(--blue-ink);margin-top:2px}
.ecard{position:absolute;top:181px;width:200px;height:305px;border-radius:10px;padding:28px 26px 0 27px}
.ecard.line{border:1.5px solid #7d98d8;background:var(--white)}
.ecard.fill{background:var(--blue-light)}
.ecard h3{font-family:"Montserrat",sans-serif;font-weight:800;font-size:19px;line-height:22px;color:var(--blue-ink);text-transform:uppercase;margin:24px 0 16px}
.ecard p{font-size:11.5px;line-height:15px;color:#2a3350;margin-bottom:8px}

/* cta */
.cta{height:422px;background:radial-gradient(ellipse at 50% 100%,#3a3020 0%,#1a1e2e 40%,var(--navy) 100%)}
.cta .photo{position:absolute;inset:0}
.cta h2{left:0;width:1200px;top:95px;text-align:center;color:var(--white);font-size:33px;line-height:46px}
.cta h2 em{font-style:normal;color:var(--blue)}
.cta .btn{left:510px;top:265px;width:180px;height:50px;font-size:17px}

/* footer */
.footer{height:563px;background:radial-gradient(circle at 90% 10%,#1a55d0 0%,var(--blue) 40%,var(--blue-deep) 100%);color:var(--white)}
.footer .big{left:0;width:1200px;top:60px;text-align:center;font-size:108px;letter-spacing:18px;line-height:120px}
.fbrands{left:0;width:1200px;top:240px;display:flex;justify-content:center;align-items:center}
.fbrand{text-align:center;width:250px}
.fbrand .wordmark{font-size:34px;letter-spacing:5px;line-height:36px}
.fbrand .tag{font-family:"Montserrat",sans-serif;font-weight:600;font-size:13px;letter-spacing:6px;margin-top:2px}
.fbrands .sep{width:2px;height:62px;background:var(--white);margin:0 38px}
.fnav{left:0;width:1200px;top:354px;display:flex;justify-content:center;gap:28px;font-size:14px;text-transform:uppercase}
.fcontact{left:0;width:1200px;top:405px;display:flex;justify-content:center;gap:36px;font-size:14px}
.fcontact span{display:flex;align-items:center;gap:9px}
.footer .hr{left:303px;top:458px;width:616px;height:1px;background:rgba(255,255,255,.5)}
.copy{left:0;width:1200px;top:496px;text-align:center;font-size:12px}
</style>
</head>
<body>

<header class="hero">
  <div class="photo" role="img" aria-label="Night sky over a transmission tower with glowing power lines at dusk"></div>
  <div class="abs wordmark nav-logo">VOLNAR</div>
  <nav class="abs nav">
    <span class="active">HOME</span><span>ABOUT US</span><span>SERVICES</span><span>VOLNAR ENERGY</span><span>VOLNAR ENGINEERING</span><span>CONTACT</span>
  </nav>
  <h1 class="abs h hero-title">Smarter <em>energy and<br>engineering</em> solutions for<br>a sustainable future</h1>
  <div class="btn btn-blue" style="left:390px;top:295px;width:199px;height:48px;font-size:13px">Volnar Engineering</div>
  <div class="btn btn-blue" style="left:610px;top:295px;width:198px;height:48px;font-size:13px">Volnar Energy</div>
  <div class="abs dots"><i class="on"></i><i></i><i></i><i></i></div>
</header>

<section class="welcome">
  <div class="abs photo" role="img" aria-label="Technician using a tablet with energy dashboards beside industrial equipment"></div>
  <h2 class="abs h">Welcome to<br>Volnar</h2>
  <div class="rule"></div>
  <p class="abs">Lorem ipsum dolor sit amet, consectetur adipiscing elit, sed do eiusmod tempor incididunt ut labore et dolore magna aliqua. Ut enim ad minim veniam, quis nostrud exercitation ullamco laboris nisi ut aliquip ex ea commodo consequat. Duis aute irure dolor in reprehenderit in voluptate velit esse cillum dolore eu fugiat nulla pariatur. Excepteur sint occaecat cupidatat non proident, sunt in culpa qui officia deserunt mollit anim id est laborum</p>
  <div class="btn btn-white" style="left:659px;top:364px;width:135px;height:38px;font-size:13px">Read more</div>
</section>

<section class="core">
  <h2 class="abs h">Our <em>core</em> areas</h2>
  <div class="rule"></div>
  <div class="area one">
    <div class="photo" role="img" aria-label="Technician installing HVAC ductwork"></div>
    <div class="brandrow"><span class="wordmark">VOLNAR</span><span class="sep"></span><span class="sub">Volnar<br>Engineering</span></div>
    <p>Technical consulting in HVAC, heating, cooling, and energy systems for commercial installations.</p>
    <div class="btn btn-blue">Read more</div>
  </div>
  <div class="area two">
    <div class="photo" role="img" aria-label="Engineer in a safety vest among battery storage cabinets"></div>
    <div class="brandrow"><span class="wordmark">VOLNAR</span><span class="sep"></span><span class="sub">Volnar<br>Energy</span></div>
    <p>Subscription-based energy monitoring and optimization services for ongoing efficiency improvement.</p>
    <div class="btn btn-blue">Read more</div>
  </div>
</section>

<section class="why">
  <svg class="abs band" width="660" height="510" viewBox="0 0 660 510" role="img" aria-label="Blue panel over a photo of hands working with a control interface">
    <defs><linearGradient id="whyFill" x1="0" y1="0" x2="1" y2="1"><stop offset="0" stop-color="#0d47c0"/><stop offset="0.6" stop-color="#1a5ad0"/><stop offset="1" stop-color="#0a3596"/></linearGradient></defs>
    <path d="M0 0H548C610 120 655 260 640 370C632 430 585 480 548 510H0Z" fill="url(#whyFill)"/>
  </svg>
  <div class="abs wordmark big">VOLNAR</div>
  <h2 class="abs h">Why<br>choose us</h2>
  <div class="rule"></div>
  <p class="abs">Lorem ipsum dolor sit amet, consectetur adipiscing elit, sed do eiusmod tempo.</p>
  <div class="btn btn-white">Contact us</div>

  <div class="feat" style="left:564px;top:46px">
    <div class="ico"><svg width="34" height="34" viewBox="0 0 24 24" fill="none" stroke="#0d47c0" stroke-width="1.8" stroke-linecap="round"><path d="M9 18h6M10 21h4M12 3a6 6 0 0 0-3.5 10.9c.6.5 1 1.2 1 2.1h5c0-.9.4-1.6 1-2.1A6 6 0 0 0 12 3z"/></svg></div>
    <div class="txt"><h3>Innovation</h3><p>Lorem ipsum dolor sit amet, consectetur adipiscing elit, sed do eiusmod tempor incididunt ut labore et dolore.</p></div>
  </div>
  <div class="feat" style="left:599px;top:158px">
    <div class="ico"><svg width="34" height="34" viewBox="0 0 24 24" fill="none" stroke="#0d47c0" stroke-width="1.8" stroke-linecap="round"><circle cx="10" cy="7" r="4"/><path d="M3 21c0-4 3-7 7-7"/><circle cx="17" cy="17" r="3"/><path d="M17 12v2M17 20v2M12 17h2M20 17h2"/></svg></div>
    <div class="txt"><h3>Technical expertise</h3><p>Lorem ipsum dolor sit amet, consectetur adipiscing elit, sed do eiusmod tempor incididunt ut labore et dolore.</p></div>
  </div>
  <div class="feat" style="left:605px;top:278px">
    <div class="ico"><svg width="34" height="34" viewBox="0 0 24 24" fill="none" stroke="#0d47c0" stroke-width="1.8" stroke-linecap="round"><path d="M4 20h16M6 17v-4M10 17v-7M14 17v-5M18 17V7M5 10l5-4 4 3 5-5"/></svg></div>
    <div class="txt"><h3>Data-driven insights</h3><p>Lorem ipsum dolor sit amet, consectetur adipiscing elit, sed do eiusmod tempor incididunt ut labore et dolore.</p></div>
  </div>
  <div class="feat" style="left:558px;top:394px">
    <div class="ico"><svg width="34" height="34" viewBox="0 0 24 24" fill="none" stroke="#0d47c0" stroke-width="1.8" stroke-linecap="round"><circle cx="12" cy="12" r="9"/><path d="M12 17v-6M12 11c0-3 2-5 5-5 0 3-2 5-5 5zM12 13c0-2-1.5-4-4-4 0 2.5 1.5 4 4 4z"/></svg></div>
    <div class="txt"><h3>Sustainability</h3><p>Lorem ipsum dolor sit amet, consectetur adipiscing elit, sed do eiusmod tempor incididunt ut labore et dolore.</p></div>
  </div>
</section>

<section class="energy">
  <div class="abs mark"><div class="wordmark">VOLNAR</div><div class="tag">ENERGY</div></div>
  <div class="ecard line" style="left:147px">
    <svg width="48" height="48" viewBox="0 0 24 24" fill="#0d47c0"><path d="M4 4h6v2a2 2 0 1 0 4 0V4h6v6h-2a2 2 0 1 0 0 4h2v6h-6v-2a2 2 0 1 0-4 0v2H4v-6h2a2 2 0 1 0 0-4H4z"/></svg>
    <h3>Energy<br>logic</h3>
    <p>Energy Logic is a module for real-time optimization of energy consumption via logical alarms that indicate deviations from optimal operation. Follow-up and reporting of deviations with proposed measures.</p>
  </div>
  <div class="ecard fill" style="left:382px">
    <svg width="48" height="48" viewBox="0 0 24 24" fill="none" stroke="#0d47c0" stroke-width="1.6" stroke-linecap="round"><circle cx="11" cy="10" r="6"/><path d="M15.5 14.5L21 20M8.5 12v-2M11 12V8M13.5 12v-3"/></svg>
    <h3>Energy<br>insight</h3>
    <p>Web-based interface for energy reporting</p>
    <p>Historical data analysis as of 2023</p>
    <p>Export of reports to spreadsheet/PDF</p>
  </div>
  <div class="ecard line" style="left:611px">
    <svg width="48" height="48" viewBox="0 0 24 24" fill="none" stroke="#0d47c0" stroke-width="1.6" stroke-linecap="round"><circle cx="12" cy="12" r="9"/><circle cx="12" cy="12" r="5.5"/><path d="M9.5 14l2-2 1.2 1.2L15 10.5"/></svg>
    <h3>Energy<br>optimize</h3>
    <p>Energy Optimize includes optimization of technical installations, the work includes setting all basic values, starting optimization functions in the existing control system, follow-up and fine-tuning for 30 days.</p>
  </div>
  <div class="ecard line" style="left:846px">
    <svg width="48" height="48" viewBox="0 0 24 24" fill="none" stroke="#0d47c0" stroke-width="1.6" stroke-linecap="round"><rect x="4" y="3" width="13" height="18" rx="1.5"/><path d="M7 8h7M7 12h4M7 16h3"/><circle cx="18" cy="17" r="3"/></svg>
    <h3>Energy<br>audit</h3>
    <p>The Energy Audit includes an analysis of energy use in the store and calculation of possible savings with proposed measures.</p>
  </div>
</section>

<section class="cta">
  <div class="photo" role="img" aria-label="Silhouetted power pylons against a dark sky with glowing lines"></div>
  <h2 class="abs h">Ready to take your <em>energy and<br>engineering</em> performance<br>to the next level?</h2>
  <div class="btn btn-blue">Get in touch</div>
</section>

<footer class="footer">
  <div class="abs wordmark big">VOLNAR</div>
  <div class="abs fbrands">
    <div class="fbrand"><div class="wordmark">VOLNAR</div><div class="tag">ENGINEERING</div></div>
    <span class="sep"></span>
    <div class="fbrand"><div class="wordmark">VOLNAR</div><div class="tag">ENERGY</div></div>
  </div>
  <nav class="abs fnav"><span>Home</span><span>About us</span><span>Services</span><span>Volnar energy</span><span>Volnar engineering</span><span>Contact</span></nav>
  <div class="abs fcontact">
    <span><svg width="14" height="16" viewBox="0 0 24 24" fill="#fff"><path d="M12 2a7 7 0 0 0-7 7c0 5 7 13 7 13s7-8 7-13a7 7 0 0 0-7-7zm0 9.5A2.5 2.5 0 1 1 12 6.5a2.5 2.5 0 0 1 0 5z"/></svg>418 Harlow Avenue&nbsp;&nbsp;Marlow Bay, NV</span>
    <span><svg width="16" height="16" viewBox="0 0 24 24" fill="#fff"><path d="M6.6 10.8a15 15 0 0 0 6.6 6.6l2.2-2.2c.3-.3.7-.4 1-.2 1.1.4 2.3.6 3.6.6.6 0 1 .4 1 1V20c0 .6-.4 1-1 1A17 17 0 0 1 3 4c0-.6.4-1 1-1h3.5c.6 0 1 .4 1 1 0 1.3.2 2.5.6 3.6.1.3 0 .7-.2 1z"/></svg>1 800 555 0147</span>
    <span><svg width="17" height="14" viewBox="0 0 24 20" fill="#fff"><path d="M2 2h20v16H2zM3 3.5l9 7 9-7v1.5l-9 7-9-7z" fill-rule="evenodd"/></svg>info@volnar.com</span>
  </div>
  <div class="abs hr"></div>
  <div class="abs copy">Copyright © 2025 All Rights Reserved</div>
</footer>

</body>
</html>
```